Utility Contractor looking for a new website

Water and wastewater utility contractor looking to create a new website that highlights our various services. We are looking for modern web presence that can be updated with current projects and new services as we grow. We have an existing logo that we would like to incorporate into the overall design of the site
Updates

Hi, Thank you for all the design submissions. I have had some time to review and have eliminated the ones I feel are not what I am looking for. Based on the designs that remain, I am looking for a clean (not to many bold colours), modern look that is not to busy (long scrolling page), Thanks, Dean

Target Market(s)

project managers, strata boards, owners, people who make decisions as to who operates their water/wastewater system

Industry/Entity Type

Utility

Font styles to use
Sans Serif

Requirements
Must have
• A min page that describes the company and what we do, A page for each of our services that outlines the service and the benefits of it. the look must be consistent throughout. additionally each service page should have some images related to the service

```html
<!DOCTYPE html>
<html lang="en">
<head>
<meta charset="utf-8">
<title>Stillwell Utility Works Ltd</title>
<link href="https://fonts.googleapis.com/css2?family=Lato:ital,wght@0,400;0,700;1,400&family=Crimson+Text:ital@1&display=swap" rel="stylesheet">
<style>
:root{
  --navy:#0f2a4a;
  --ink:#1c2f48;
  --text:#666;
  --dark-text:#333;
  --rule:#cfcfcf;
  --page:#ececec;
  --footer:#dcdcdc;
  --bar:#3a3a3a;
  --accent-line:#4b4b4b;
  --teal:#1aa38c;
  --hero-light:#a9bccd;
  --hero-dark:#2c4a66;
}
*{margin:0;padding:0;box-sizing:border-box}
html,body{width:672px;height:1200px;overflow:hidden}
body{background:var(--page);font-family:"Lato",sans-serif;color:var(--text);position:relative}
.abs{position:absolute}
.social{display:flex;gap:9px}
.social span{width:6px;height:6px;border-radius:50%;background:var(--navy);display:block}
.top-social{left:541px;top:3px}
.brand{left:72px;top:40px;font-weight:700;font-size:15px;line-height:14px;color:var(--navy);letter-spacing:.2px;width:140px}
.nav{left:310px;top:76px;display:flex;font-style:italic;font-size:10px;color:var(--ink)}
.nav a{color:inherit;text-decoration:none;position:relative}
.nav a.home{margin-right:22px}
.nav a.home::before{content:"";position:absolute;left:-2px;right:-2px;top:-10px;height:2px;background:var(--accent-line)}
.nav .blog{margin-right:24px}.nav .port{margin-right:26px}.nav .serv{margin-right:26px}.nav .about{margin-right:22px}
.rule{left:72px;width:528px;height:1px;background:var(--rule)}
.hero{left:72px;top:119px;width:528px;height:216px;background:linear-gradient(180deg,var(--hero-dark) 0%,var(--hero-light) 50%,var(--hero-dark) 100%)}
.quote{left:130px;top:363px;width:420px;font-family:"Crimson Text",serif;font-style:italic;font-size:11.5px;line-height:15px;color:#666}
.quote b{font-family:"Lato",sans-serif;font-style:normal;font-weight:400;font-size:11px;color:var(--navy)}
.btn{left:301px;top:417px;width:70px;height:22px;border-radius:5px;background:var(--navy);color:#fff;font-size:7px;text-align:center;line-height:22px}
.dots{left:303px;top:474px}
.h2{left:72px;font-size:15.5px;color:var(--navy);font-weight:400;letter-spacing:.3px}
.svc{top:560px;width:169px}
.svc .pic{width:169px;height:121px;border:1px solid var(--teal);background:linear-gradient(180deg,#3d6fc0 0%,#6a90c8 45%,#b89a52 75%,#8a9aa8 100%)}
.svc h3{font-weight:400;font-size:10px;color:var(--navy);margin-top:8px}
.svc p{font-size:6.4px;line-height:11px;margin-top:3px;color:var(--text)}
.about-pic{left:72px;top:797px;width:264px;height:198px;background:linear-gradient(160deg,#4f7fc4 0%,#8aa6c8 35%,#5e6a76 60%,#2a2f35 100%)}
.about-text{left:360px;width:240px;font-size:6.4px;line-height:11.6px;text-align:justify}
.about-text.first{top:794px;color:var(--text)}
.about-text.second{top:881px;color:var(--dark-text)}
.footer{left:0;top:1043px;width:672px;height:125px;background:var(--footer)}
.footer-line{left:72px;top:1043px;width:528px;height:2px;background:var(--accent-line)}
.fcol{font-style:italic;color:var(--navy)}
.fcol h4{font-weight:400;font-size:9px;margin-bottom:8px}
.links{left:84px;top:1058px;font-size:6.4px;line-height:14.5px}
.touch{left:247px;top:1058px;font-size:7.6px;line-height:11px}
.touch p.addr{font-style:normal;font-size:6.4px;margin-top:4px}
.contact-btn{display:inline-block;margin-top:5px;width:44px;height:17px;border:1px solid #999;background:#e6e6e6;font-style:normal;font-size:5.6px;text-align:center;line-height:15px;color:var(--dark-text)}
.foot-social{left:376px;top:1060px}
.map{left:450px;top:1059px;width:138px;height:82px;background:linear-gradient(135deg,#e8e2cc 0%,#d9d4bf 50%,#b9cbd8 100%)}
.bottom{left:0;top:1168px;width:672px;height:32px;background:var(--bar);color:#ddd;font-size:5.6px;padding:15px 72px 0}
</style>
</head>
<body>
<div class="abs social top-social"><span></span><span></span><span></span></div>
<div class="abs brand">STILLWELL<br>UTILITY WORKS</div>
<nav class="abs nav"><a class="home">Home</a><a class="blog">Blog</a><a class="port">Portfolio</a><a class="serv">Services</a><a class="about">About</a><a>Contact</a></nav>
<div class="abs rule" style="top:99px"></div>

<div class="abs hero" role="img" aria-label="Hero photo of a water droplet falling into rippling water"></div>
<p class="abs quote">Curabitur cursus est sit amet <b>dolor pharetra rutrum</b>. Cum sociis natoque penatibus et magnis dis parturient montes, nascetur ridiculus mus.</p>
<div class="abs btn">READ MORE</div>
<svg class="abs dots" width="66" height="10" viewBox="0 0 66 10"><g fill="#777"><path d="M1 6 Q8 0 16 4 Q8 8 1 6Z"/><path d="M25 6 Q32 0 40 4 Q32 8 25 6Z"/><path d="M49 6 Q56 0 64 4 Q56 8 49 6Z"/></g></svg>
<div class="abs rule" style="top:506px"></div>

<h2 class="abs h2" style="top:525px">OUR SERVICES</h2>
<div class="abs svc" style="left:72px"><div class="pic" role="img" aria-label="Photo of colourful water slides against a blue sky"></div><h3>Water service for home</h3><p>Lorem ipsum dolor sit amet, consectetur adipiscing elit. Integer ac neque ligula.</p></div>
<div class="abs svc" style="left:252px"><div class="pic" role="img" aria-label="Photo of colourful water slides against a blue sky"></div><h3>Bottled water delivery</h3><p>Praesent vel turpis sem. Donec feugiat ultrices molestie. Suspendisse aliquet nunc non neque fermentum</p></div>
<div class="abs svc" style="left:432px"><div class="pic" role="img" aria-label="Photo of colourful water slides against a blue sky"></div><h3>Water cooler service</h3><p>Fusce bibendum ante eu urna malesuada eu dapibus magna lobortis. Integer sed nisl at velit elementum.</p></div>
<div class="abs rule" style="top:747px"></div>

<h2 class="abs h2" style="top:766px">ABOUT COMPANY</h2>
<div class="abs about-pic" role="img" aria-label="Photo of a modern glass office building under a blue sky"></div>
<p class="abs about-text first">Lorem ipsum dolor sit amet, consectetur adipiscing elit. Integer ac neque ligula. Pellentesque bibendum, lorem sit amet pretium ultricies, odio purus faucibus eros, a scelerisque orci leo ac libero. Sed fringilla ultricies rutrum. Praesent lacus magna, pharetra eu convallis at, consectetur vitae libero. Praesent vel turpis sem. Donec feugiat ultrices molestie. Suspendisse aliquet nunc non neque fermentum eget ultrices mi scelerisque.</p>
<p class="abs about-text second">Fusce bibendum ante eu urna malesuada eu dapibus magna lobortis. Integer sed nisl at velit vestibulum elementum. Cras et diam turpis. Etiam dictum lobortis felis, eu pulvinar dolor tincidunt a. Proin tincidunt, sem sed dignissim ultricies, tellus dolor scelerisque enim, sed ultrices nunc ante vestibulum odio. Morbi luctus facilisis urna, non mattis nisi ullamcorper ornare. Pellentesque habitant morbi tristique senectus et netus et malesuada fames ac turpis egestas. Phasellus lectus elit, convallis eget laoreet eget, pharetra in turpis. Nunc volutpat enim eu elit sodales luctus. Etiam vulputate tortor quis ipsum dignissim volutpat. Donec est velit, placerat in volutpat eget, consectetur a felis. Aenean in blandit ipsum. Integer sit amet rhoncus nibh. Aliquam fringilla vestibulum erat, in blandit mauris pretium nec.</p>

<footer>
<div class="abs footer"></div>
<div class="abs footer-line"></div>
<div class="abs fcol links"><h4>Quick links</h4>Home<br>Blog<br>Portfolio<br>Services<br>About<br>Contact</div>
<div class="abs fcol touch"><h4>Get in touch</h4>Stillwell Utility Works Ltd<p class="addr">XXX, XXXX, XXXXX<br>+00 000.00.0000</p><span class="contact-btn">CONTACT</span></div>
<div class="abs social foot-social"><span></span><span></span><span></span></div>
<div class="abs map" role="img" aria-label="Street map showing the office location"></div>
<div class="abs bottom">© Stillwell Utility Works 2014</div>
</footer>
</body>
</html>
```